LVNODE
biz card
LVNODE - Information Technology
Creative Brief
Professional
jun pa
238 Elmora Pl, 3FL NewYorkCity, NY 10583
jun.pa@lanviretnode.com
www.lanviretnode.com

```html
<!DOCTYPE html>
<html lang="en">
<head>
<meta charset="utf-8">
<title>LVNODE business card</title>
<link rel="stylesheet" href="https://fonts.googleapis.com/css2?family=Arimo:wght@400;700&display=swap">
<style>
  :root {
    --page-bg: #e9e6e3;
    --card-white: #ffffff;
    --brand-red: #d01f26;
    --brand-red-deep: #a8141a;
    --brand-red-light: #e2474b;
    --swoosh-black: #141414;
    --text-white: #ffffff;
  }
  * { margin: 0; padding: 0; box-sizing: border-box; }
  html, body {
    width: 1200px;
    height: 965px;
    overflow: hidden;
    background: var(--page-bg);
    font-family: "Arimo", Arial, sans-serif;
  }
  .business-card {
    position: absolute;
    left: 120px;
    top: 205px;
    width: 960px;
    height: 555px;
    border-radius: 32px;
    overflow: hidden;
    background: var(--card-white);
    box-shadow: 0 10px 28px rgba(0,0,0,0.22);
  }
  .card-waves {
    position: absolute;
    inset: 0;
    width: 100%;
    height: 100%;
  }
  .brand-lockup {
    position: absolute;
    left: 78px;
    top: 150px;
    display: flex;
    align-items: center;
    gap: 18px;
  }
  .brand-mark {
    width: 46px;
    height: 46px;
    background: var(--brand-red);
  }
  .brand-name {
    font-weight: 700;
    font-size: 56px;
    letter-spacing: 2px;
    color: var(--brand-red);
  }
  .person-name {
    position: absolute;
    right: 70px;
    top: 128px;
    font-weight: 700;
    font-size: 46px;
    color: var(--brand-red);
  }
  .office-address {
    position: absolute;
    right: 500px;
    top: 392px;
    text-align: right;
    font-size: 27px;
    line-height: 39px;
    color: var(--text-white);
  }
  .contact-list {
    position: absolute;
    left: 495px;
    top: 338px;
    list-style: none;
    font-size: 27px;
    line-height: 39px;
    color: var(--text-white);
  }
  .contact-list li {
    display: flex;
    align-items: center;
    gap: 14px;
  }
  .contact-icon {
    width: 26px;
    height: 26px;
    flex: none;
  }
</style>
</head>
<body>
  <div class="business-card">
    <svg class="card-waves" viewBox="0 0 960 555" preserveAspectRatio="none" aria-hidden="true">
      <defs>
        <linearGradient id="redBand" x1="0" y1="0" x2="1" y2="1">
          <stop offset="0" stop-color="var(--brand-red-deep)"/>
          <stop offset="0.55" stop-color="var(--brand-red)"/>
          <stop offset="1" stop-color="var(--brand-red-light)"/>
        </linearGradient>
      </defs>
      <path d="M0 285 C 160 250, 300 300, 470 310 C 640 320, 800 270, 960 235 L960 250 C 800 290, 640 338, 470 330 C 300 322, 160 300, 0 312 Z" fill="var(--swoosh-black)"/>
      <path d="M0 305 C 160 300, 300 335, 470 340 C 640 345, 800 290, 960 245 L960 555 L0 555 Z" fill="url(#redBand)"/>
    </svg>

    <div class="brand-lockup">
      <span class="brand-mark"></span>
      <span class="brand-name">LVNODE</span>
    </div>

    <div class="person-name">jun pa</div>

    <address class="office-address" style="font-style:normal">
      238 Elmora Pl, 3FL<br>
      NewYorkCity,&nbsp; NY 10583
    </address>

    <ul class="contact-list">
      <li>
        <svg class="contact-icon" viewBox="0 0 24 24"><path d="M6 3c1 0 2 3 2.5 4.5.3 1-1.5 2-1.2 3 .8 2.2 2.6 4 4.8 4.8 1 .3 2-1.5 3-1.2C16.6 14.6 20 16 20 17c0 1.5-2 3.5-3.5 3.5C10 20.5 3.5 14 3.5 7.5 3.5 5 5 3 6 3z" fill="#fff"/></svg>
        212-604-2817
      </li>
      <li>
        <svg class="contact-icon" viewBox="0 0 24 24"><rect x="7" y="2" width="10" height="20" rx="2" fill="#fff"/><rect x="9" y="5" width="6" height="9" fill="#c4161c"/></svg>
        212-604-2817
      </li>
      <li>
        <svg class="contact-icon" viewBox="0 0 24 24"><rect x="7" y="3" width="10" height="6" fill="#fff"/><rect x="3" y="9" width="18" height="8" rx="1.5" fill="#fff"/><rect x="7" y="15" width="10" height="6" fill="#fff"/><rect x="8.5" y="16.5" width="7" height="3" fill="#c4161c"/></svg>
        212-604-2817
      </li>
      <li>
        <svg class="contact-icon" viewBox="0 0 24 24"><circle cx="12" cy="12" r="4" fill="none" stroke="#fff" stroke-width="2.4"/><path d="M16 12v1.5a2.5 2.5 0 0 0 5 0V12a9 9 0 1 0-3.5 7.1" fill="none" stroke="#fff" stroke-width="2.4"/></svg>
        jun.pa@lanviretnode.com
      </li>
      <li>
        <svg class="contact-icon" viewBox="0 0 24 24"><circle cx="12" cy="12" r="9" fill="none" stroke="#fff" stroke-width="2"/><ellipse cx="12" cy="12" rx="4" ry="9" fill="none" stroke="#fff" stroke-width="1.6"/><path d="M3 12h18M5 7h14M5 17h14" stroke="#fff" stroke-width="1.4"/></svg>
        www.lanviretnode.com
      </li>
    </ul>
  </div>
</body>
</html>
```